Banner Ad Design Project

I need 4 campaigns to have banners made, 6 banner sizes each so 24 total banners. Here are the landing pages with the messaging.

http://www.brightvalelistings.example/Oxwell-Care-Health-Insurance-48207.html

http://www.brightvalelistings.example/Marlow-Crest-Lending-48206.html
Marlow Crest Lending: Get Cash! Stay in Your Home! Then below in smaller lettering Find out if a reverse mortgage is right for you!

http://www.brightvalelistings.example/Vexmo-Direct-48205.html
Vexmo: Is Your Family Protected? Then in smaller lettering Call NOW for a FREE home security evaluation

http://www.brightvalelistings.example/LedgerSafeHelp-48217.html
Ledger Safe Helpers: We’ll help solve your IRS tax problems then in smaller lettering, Call today to find out how we can help!

Need to get done asap. Much more work can be following right after. Here are the sizes

300 X 50
300x250
320 X50
216 X36
168 X 28
120 X 20
Updates

I need final designs to choose from right now. I need to make a selection to get the banners done immediately. thanks

Industry/Entity Type

Security

Requirements
Must have
• Phone number call to action

```html
<!DOCTYPE html>
<html lang="en">
<head>
<meta charset="utf-8">
<title>Oxwell Health Insurance – Banner Set</title>
<link rel="stylesheet" href="https://fonts.googleapis.com/css2?family=Open+Sans:wght@400;600;700&display=swap">
<style>
  :root {
    --stage-light: #c4c4c4;
    --stage-dark: #858585;
    --blue-top: #3a8cc8;
    --blue-mid: #1d6aa5;
    --blue-deep: #0f4f80;
    --orange: #f28c1c;
    --orange-box: #f7941d;
    --white: #ffffff;
    --ink: #1b1b1b;
    --band-light: #fafafa;
    --band-shade: #d3d6d9;
  }
  * { box-sizing: border-box; margin: 0; padding: 0; }
  html, body { width: 899px; height: 1200px; overflow: hidden; }
  body {
    position: relative;
    font-family: "Open Sans", Arial, sans-serif;
    background: radial-gradient(ellipse at 50% 20%, var(--stage-light) 0%, #a6a6a6 55%, var(--stage-dark) 100%);
  }

  /* ---------- shared ---------- */
  .banner {
    position: absolute;
    overflow: hidden;
    color: var(--white);
    box-shadow: 0 0.1em 0.3em rgba(0,0,0,0.3);
  }
  .brand { position: absolute; display: flex; align-items: center; white-space: nowrap; }
  .brand-dot { display: block; flex: none; border-radius: 50%; background: var(--orange); }
  .brand-name { font-weight: 700; color: var(--orange); letter-spacing: -0.02em; line-height: 1; }
  .tagline { position: absolute; white-space: nowrap; }
  .tagline-text { display: block; font-weight: 700; letter-spacing: -0.01em; }
  .cta-title {
    position: absolute; text-align: center; white-space: nowrap;
  }
  .cta-title-text { display: block; font-weight: 700; line-height: 1; }
  .cta-phone {
    position: absolute; display: flex; align-items: center; justify-content: center;
    background: var(--orange-box); white-space: nowrap;
  }
  .cta-phone-text { line-height: 1; }

  /* ---------- strip banners: 1em = 1 design unit of 10 px at 300x50 ---------- */
  .banner--strip {
    width: 30em; height: 5em;
    background: linear-gradient(180deg, var(--blue-top) 0%, var(--blue-mid) 55%, var(--blue-deep) 100%);
    border-top: 0.08em solid rgba(255,255,255,0.6);
  }
  .banner--strip .brand { left: 0.4em; top: 1.55em; gap: 0.35em; }
  .banner--strip .brand-dot { width: 1em; height: 1em; }
  .banner--strip .brand-name { font-size: 1.65em; }
  .banner--strip .tagline { left: 8.6em; top: 1.1em; }
  .banner--strip .tagline-text { font-size: 1.3em; line-height: 1.12; }
  .banner--strip .cta-title { left: 17.7em; top: 0.45em; width: 11.3em; }
  .banner--strip .cta-title-text { font-size: 1.45em; }
  .banner--strip .cta-phone { left: 17.7em; top: 2.5em; width: 11.3em; height: 2.1em; }
  .banner--strip .cta-phone-text { font-size: 1.28em; font-weight: 600; }

  .size-120x20 { left: 324px; top: 85px;  font-size: 8.43px; }
  .size-168x28 { left: 273px; top: 142px; font-size: 11.83px; }
  .size-216x36 { left: 222px; top: 226px; font-size: 15.23px; }
  .size-300x50 { left: 133px; top: 326px; font-size: 21.1px; }
  .size-320x50 { left: 112px; top: 460px; font-size: 21.15px; width: 32em; }
  .size-320x50 .tagline { left: 9.6em; }
  .size-320x50 .cta-title,
  .size-320x50 .cta-phone { left: 19.3em; width: 11.2em; }

  /* ---------- medium rectangle 300x250 ---------- */
  .banner--rect {
    left: 133px; top: 599px; font-size: 21.1px;
    width: 30em; height: 25em;
    background: var(--blue-deep);
  }
  .rect-topline { position: absolute; left: 0; top: 0; width: 100%; height: 0.8em; background: linear-gradient(180deg, #ffffff, #e1e7ec); }
  .rect-hero {
    position: absolute; left: 0; top: 0.8em; width: 100%; height: 10.9em;
    background: linear-gradient(180deg, var(--blue-top) 0%, var(--blue-mid) 60%, var(--blue-deep) 100%);
  }
  .rect-afford {
    position: absolute; left: 0; top: 11.7em; width: 100%; height: 4em;
    background: linear-gradient(180deg, var(--band-light) 0%, #ececec 55%, var(--band-shade) 100%);
  }
  .rect-afford-text {
    position: absolute; right: 1.9em; top: 1.25em; white-space: nowrap;
    font-size: 1.75em; font-weight: 400; color: var(--ink); line-height: 1; letter-spacing: -0.01em;
  }
  .rect-call {
    position: absolute; left: 0; top: 15.7em; width: 100%; height: 9.3em;
    background: linear-gradient(180deg, var(--blue-mid) 0%, #165e96 50%, var(--blue-deep) 100%);
  }
  .banner--rect .brand { left: 1.1em; top: 4.3em; gap: 0.5em; }
  .banner--rect .brand-dot { width: 1.8em; height: 1.8em; }
  .banner--rect .brand-name { font-size: 3.5em; }
  .banner--rect .tagline { left: 17.4em; top: 1.75em; width: 11.4em; text-align: center; }
  .banner--rect .tagline-text { font-size: 2.25em; line-height: 1.38; font-weight: 600; }
  .banner--rect .cta-title { left: 0; top: 16.95em; width: 100%; }
  .banner--rect .cta-title-text { font-size: 2.4em; }
  .banner--rect .cta-phone { left: 6.2em; top: 20.2em; width: 17.7em; height: 3.9em; }
  .banner--rect .cta-phone-text { font-size: 2.1em; font-weight: 400; }
</style>
</head>
<body>

  <section class="banner banner--strip size-120x20" aria-label="Oxwell health insurance banner 120 by 20">
    <div class="brand"><span class="brand-dot"></span><span class="brand-name">Oxwell</span></div>
    <p class="tagline"><span class="tagline-text">Great Health<br>Insurance</span></p>
    <p class="cta-title"><span class="cta-title-text">Call Today!</span></p>
    <p class="cta-phone"><span class="cta-phone-text">(888) 555-0147</span></p>
  </section>

  <section class="banner banner--strip size-168x28" aria-label="Oxwell health insurance banner 168 by 28">
    <div class="brand"><span class="brand-dot"></span><span class="brand-name">Oxwell</span></div>
    <p class="tagline"><span class="tagline-text">Great Health<br>Insurance</span></p>
    <p class="cta-title"><span class="cta-title-text">Call Today!</span></p>
    <p class="cta-phone"><span class="cta-phone-text">(888) 555-0147</span></p>
  </section>

  <section class="banner banner--strip size-216x36" aria-label="Oxwell health insurance banner 216 by 36">
    <div class="brand"><span class="brand-dot"></span><span class="brand-name">Oxwell</span></div>
    <p class="tagline"><span class="tagline-text">Great Health<br>Insurance</span></p>
    <p class="cta-title"><span class="cta-title-text">Call Today!</span></p>
    <p class="cta-phone"><span class="cta-phone-text">(888) 555-0147</span></p>
  </section>

  <section class="banner banner--strip size-300x50" aria-label="Oxwell health insurance banner 300 by 50">
    <div class="brand"><span class="brand-dot"></span><span class="brand-name">Oxwell</span></div>
    <p class="tagline"><span class="tagline-text">Great Health<br>Insurance</span></p>
    <p class="cta-title"><span class="cta-title-text">Call Today!</span></p>
    <p class="cta-phone"><span class="cta-phone-text">(888) 555-0147</span></p>
  </section>

  <section class="banner banner--strip size-320x50" aria-label="Oxwell health insurance banner 320 by 50">
    <div class="brand"><span class="brand-dot"></span><span class="brand-name">Oxwell</span></div>
    <p class="tagline"><span class="tagline-text">Great Health<br>Insurance</span></p>
    <p class="cta-title"><span class="cta-title-text">Call Today!</span></p>
    <p class="cta-phone"><span class="cta-phone-text">(888) 555-0147</span></p>
  </section>

  <section class="banner banner--rect" aria-label="Oxwell health insurance banner 300 by 250">
    <div class="rect-topline"></div>
    <div class="rect-hero"></div>
    <div class="rect-afford"><p class="rect-afford-text">You can Actually Afford</p></div>
    <div class="rect-call"></div>
    <div class="brand"><span class="brand-dot"></span><span class="brand-name">Oxwell</span></div>
    <p class="tagline"><span class="tagline-text">Great<br>Health<br>Insurance</span></p>
    <p class="cta-title"><span class="cta-title-text">Call Today!</span></p>
    <p class="cta-phone"><span class="cta-phone-text">(888) 555-0147</span></p>
  </section>

</body>
</html>
```